We Are Corvane Marketing Collateral

We Are Corvane has undergone a rebrand with new logo, website, and intranet design builds. The business is now looking to update its marketing collateral with the new logo design and colour palette. Deliverables include PowerPoint template, Report template, Letterhead, and Email signature. Refer attached design brief for more information. Also attached are the logo and brand document.
Target Market(s)
Executive & Board of SME impact organisations.
Industry/Entity Type
We serve small to medium organisations who are delivering impact, not-for-profits, social enterprises and purpose driven organisations.
Font styles to use
Other font styles liked:
- Roca Two Thin, Rubik Regular
Look and feel
Each slider illustrates characteristics of the customer's brand and the style your logo design should communicate.

```html
<!DOCTYPE html>
<html lang="en">
<head>
<meta charset="utf-8">
<title>Corvane Stationery</title>
<link rel="stylesheet" href="https://fonts.googleapis.com/css2?family=Open+Sans:wght@400;600&display=swap">
<style>
  :root {
    --backdrop: #e6e6e6;
    --paper: #ffffff;
    --brand-green: #255651;
    --ink: #5a5a5a;
    --ink-soft: #6e6e6e;
    --accent-green: #4aa56f;
    --accent-red: #e0575a;
    --accent-magenta: #b0457f;
    --accent-orange: #e8873e;
    --accent-teal: #2f9aa5;
  }
  * { box-sizing: border-box; margin: 0; padding: 0; }
  html, body { width: 1200px; height: 795px; overflow: hidden; }
  body {
    background: var(--backdrop);
    font-family: "Open Sans", Arial, sans-serif;
    color: var(--ink);
    position: relative;
  }

  /* Letterhead */
  .letterhead {
    position: absolute;
    left: 110px; top: 70px;
    width: 460px; height: 650px;
    background: var(--paper);
    box-shadow: 0 2px 6px rgba(0,0,0,0.12);
  }
  .letterhead__brand {
    position: absolute; left: 44px; top: 40px;
    display: flex; align-items: center; gap: 10px;
  }
  .brand-dot {
    width: 34px; height: 34px; border-radius: 50%;
    background: var(--accent-teal);
  }
  .brand-name {
    font-size: 24px; font-weight: 400; letter-spacing: 2px;
    color: var(--brand-green); text-transform: uppercase;
  }
  .letterhead__contact {
    position: absolute; right: 44px; top: 108px;
    font-size: 8.5px; line-height: 13px; color: var(--ink-soft);
    list-style: none;
  }
  .letterhead__contact li { display: flex; align-items: center; gap: 5px; }
  .letterhead__contact svg { width: 8px; height: 8px; fill: var(--brand-green); }
  .letterhead__contact .no-icon { padding-left: 13px; }

  .letter {
    position: absolute; left: 44px; top: 178px; width: 372px;
    font-size: 8.3px; line-height: 12.5px; color: var(--ink);
  }
  .letter p { margin-bottom: 11px; }
  .letter__salutation { margin-bottom: 9px; }
  .letter__signature {
    width: 62px; height: 34px; margin-top: 6px;
    background: linear-gradient(90deg, #e9ebf0, #dfe2ea);
    border-radius: 3px;
  }

  .letterhead__stripe {
    position: absolute; left: 0; right: 0; bottom: 14px; height: 3px;
    display: flex;
  }
  .letterhead__stripe span { flex: 1; }
  .stripe--green { background: var(--accent-green); }
  .stripe--red { background: var(--accent-red); }
  .stripe--magenta { background: var(--accent-magenta); }
  .stripe--orange { background: var(--accent-orange); }
  .letterhead__band {
    position: absolute; left: 0; right: 0; bottom: 0; height: 14px;
    background: var(--brand-green);
  }

  /* Envelope (back view) */
  .envelope {
    position: absolute;
    left: 620px; top: 300px;
    width: 520px; height: 260px;
    background: var(--paper);
    box-shadow: 0 2px 6px rgba(0,0,0,0.12);
    overflow: hidden;
  }
  .envelope__flap {
    position: absolute; left: 0; top: 0; width: 100%; height: 116px;
    background: var(--brand-green);
    border-radius: 0 0 10px 10px;
    display: flex; align-items: center; justify-content: center; gap: 8px;
  }
  .envelope__flap .brand-dot { width: 26px; height: 26px; }
  .envelope__flap .brand-name { font-size: 18px; color: var(--paper); }
</style>
</head>
<body>

<section class="letterhead">
  <div class="letterhead__brand">
    <span class="brand-dot"></span>
    <span class="brand-name">Corvane</span>
  </div>

  <ul class="letterhead__contact">
    <li class="no-icon">48 Alder Lane, Suite 6</li>
    <li class="no-icon">Marlow, MA 01742</li>
    <li><svg viewBox="0 0 10 10"><path d="M2 0.5 L3.6 0.5 L4.2 2.8 L3 3.6 Q4 5.8 6.4 7 L7.2 5.8 L9.5 6.4 L9.5 8 Q9.5 9.5 8 9.5 Q0.5 8.5 0.5 2 Q0.5 0.5 2 0.5Z"/></svg>(555) 318-4920</li>
    <li><svg viewBox="0 0 10 10"><path d="M0.5 2 H9.5 V8.5 H0.5Z M1.2 2.6 L5 5.6 L8.8 2.6 V2.5 H1.2Z" fill-rule="evenodd"/></svg>info@corvane.com</li>
    <li><svg viewBox="0 0 10 10"><circle cx="5" cy="5" r="4.3" fill="none" stroke="#255651" stroke-width="1"/><path d="M0.7 5 H9.3 M5 0.7 Q2.5 5 5 9.3 M5 0.7 Q7.5 5 5 9.3" fill="none" stroke="#255651" stroke-width="0.8"/></svg>www.corvaneweb.com</li>
  </ul>

  <div class="letter">
    <p class="letter__salutation">Dear customer,</p>
    <p>Lorem ipsum dolor sit amet, consectetur adipisicing elit, sed do eiusmod tempor incididunt ut labore et dolore magna aliqua. Ut enim ad minim veniam, quis nostrud exercitation ullamco laboris nisi ut aliquip ex ea commodo consequat. Duis aute irure dolor in reprehenderit in voluptate velit esse cillum dolore eu fugiat nulla pariatur. Excepteur sint occaecat cupidatat non proident, sunt in culpa qui officia deserunt mollit anim id est laborum.</p>
    <p>Lorem ipsum dolor sit amet, consectetur adipisicing elit, sed do eiusmod tempor incididunt ut labore et dolore magna aliqua. Ut enim ad minim veniam, quis nostrud exercitation ullamco laboris nisi ut aliquip ex ea commodo consequat. Duis aute irure dolor in reprehenderit in voluptate velit esse cillum dolore eu fugiat nulla pariatur. Excepteur sint occaecat cupidatat non proident, sunt in culpa qui officia deserunt mollit anim id est laborum.</p>
    <p>Lorem ipsum dolor sit amet, consectetur adipisicing elit, sed do eiusmod tempor incididunt ut labore et dolore magna aliqua. Ut enim ad minim veniam, quis nostrud exercitation ullamco laboris nisi ut aliquip ex ea commodo consequat. Duis aute irure dolor in reprehenderit in voluptate velit esse cillum dolore eu fugiat nulla pariatur. Excepteur sint occaecat cupidatat non proident, sunt in culpa qui officia deserunt mollit anim id est laborum.</p>
    <p>Lorem ipsum dolor sit amet, consectetur adipisicing elit, sed do eiusmod tempor incididunt ut labore et dolore magna aliqua. Ut enim ad minim veniam, quis nostrud exercitation ullamco laboris nisi ut aliquip ex ea commodo consequat. Duis aute irure dolor in reprehenderit.</p>
    <p class="letter__closing">Yours Sincerely,</p>
    <div class="letter__signature" role="img" aria-label="Handwritten signature"></div>
  </div>

  <div class="letterhead__stripe">
    <span class="stripe--green"></span>
    <span class="stripe--red"></span>
    <span class="stripe--magenta"></span>
    <span class="stripe--orange"></span>
  </div>
  <div class="letterhead__band"></div>
</section>

<section class="envelope">
  <div class="envelope__flap">
    <span class="brand-dot"></span>
    <span class="brand-name">Corvane</span>
  </div>
</section>

</body>
</html>
```